Business Cards, Letterheads, Envelopes

A company's new identity to be reflected on its stationery items

Target Market(s)

Large Corporate Companies & Enterprises

Font styles to use
Sans Serif

Colors
0555a3
3176b5
85abd2
85cae6
33a6d7
0293ce

```html
<!DOCTYPE html>
<html lang="en">
<head>
<meta charset="utf-8">
<title>Nordvane Systems — Stationery</title>
<link rel="stylesheet" href="https://fonts.googleapis.com/css2?family=Didact+Gothic&family=Roboto:wght@400&display=swap">
<style>
  :root {
    --backdrop: #dcdcdc;
    --paper: #f6f6f6;
    --brand: #3388c9;
    --brand-deep: #3176b5;
    --brand-faint: #e4e9ef;
    --ink: #3a3a3a;
    --ink-soft: #4a4a4a;
  }
  * { box-sizing: border-box; margin: 0; padding: 0; }
  html, body { width: 1200px; height: 877px; overflow: hidden; }
  body { background: var(--backdrop); position: relative; font-family: "Didact Gothic", sans-serif; color: var(--ink); }

  .sheet { position: absolute; background: var(--paper); box-shadow: 0 2px 8px rgba(0,0,0,.12); overflow: hidden; }

  /* Letterhead */
  .letterhead { left: 69px; top: 64px; width: 527px; height: 742px; }
  .brand-lockup { position: absolute; display: flex; align-items: center; gap: 7px; color: var(--brand); font-family: "Didact Gothic", sans-serif; }
  .brand-dot { width: 40px; height: 40px; border-radius: 50%; background: var(--brand); flex: none; }
  .brand-name { font-size: 11px; line-height: 1.15; letter-spacing: .08em; text-transform: uppercase; }
  .brand-name span { display: block; }
  .brand-name .legal { font-size: 7.5px; letter-spacing: .18em; }
  .letterhead .brand-lockup { left: 182px; top: 64px; }

  .watermark { position: absolute; border-radius: 50%; background: var(--brand-faint); opacity: .55; }
  .letterhead .watermark { left: 160px; top: 240px; width: 210px; height: 210px; }

  .letter { position: absolute; left: 45px; top: 204px; width: 438px; }
  .salutation { font-size: 13.6px; margin-bottom: 24px; }
  .letter p { font-size: 7.9px; line-height: 11.4px; color: var(--ink-soft); margin-bottom: 11.4px; text-align: justify; }
  .closing { position: absolute; left: 45px; top: 488px; font-size: 7.9px; color: var(--ink-soft); }
  .signature { position: absolute; left: 41px; top: 518px; width: 95px; height: 40px; background: linear-gradient(90deg, rgba(5,85,163,.18), rgba(5,85,163,.08)); border-radius: 3px; }
  .letter-footer { position: absolute; left: 0; right: 0; top: 694px; text-align: center; font-family: "Roboto", sans-serif; font-size: 8px; line-height: 12px; color: var(--ink-soft); }

  /* Envelope back */
  .envelope-back { left: 614px; top: 269px; width: 531px; height: 240px; }
  .envelope-flap { position: absolute; left: 0; top: 0; width: 531px; height: 74px; }
  .flap-content { position: absolute; left: 0; right: 0; top: 22px; text-align: center; color: #fff; }
  .flap-name { font-size: 11px; letter-spacing: .1em; text-transform: uppercase; }
  .flap-url { margin-top: 10px; font-family: "Roboto", sans-serif; font-size: 7.4px; letter-spacing: .14em; font-style: normal; }

  /* Envelope front */
  .envelope-front { left: 614px; top: 562px; width: 533px; height: 242px; }
  .envelope-front .brand-lockup { left: 23px; top: 21px; gap: 5px; }
  .envelope-front .brand-dot { width: 30px; height: 30px; }
  .envelope-front .brand-name { font-size: 8.5px; }
  .envelope-front .brand-name .legal { font-size: 6px; }
  .return-address { position: absolute; left: 23px; top: 60px; font-family: "Roboto", sans-serif; font-size: 7.8px; line-height: 10px; color: var(--ink); font-style: normal; }
  .envelope-front .watermark { left: 340px; top: 30px; width: 170px; height: 170px; }
</style>
</head>
<body>

  <section class="sheet letterhead">
    <div class="brand-lockup">
      <div class="brand-dot"></div>
      <div class="brand-name"><span>Nordvane Systems</span><span class="legal">Private Limited</span></div>
    </div>
    <div class="watermark"></div>

    <div class="letter">
      <p class="salutation">Dear Mr. Carver,</p>
      <p>Lorem ipsum dolor sit amet, consectetur adipiscing elit. Donec orci purus, luctus vitae dignissim eu, iaculis sed purus. Vivamus faucibus, ipsum nec aliquet viverra, leo mauris condimentum ligula, sit amet sagittis enim ligula quis arcu. Nam egestas tortor id nisi porttitor mattis. In tortor ante, ultricies in suscipit a, tempus non massa. Vivamus et auctor mi. Fusce vel massa nulla. Phasellus nec eros mauris, et scelerisque orci.</p>
      <p>Donec malesuada orci vitae nulla accumsan porta a id massa. Quisque accumsan iaculis magna sit amet fringilla. Maecenas consequat, magna eget tincidunt semper, odio nibh rutrum mi, id feugiat ante nisi eu risus. Vestibulum nunc orci, rhoncus a placerat in, ultricies in mi. Cras mattis varius eros, vel fringilla nisi suscipit eget. Quisque scelerisque sagittis nulla at porttitor.</p>
      <p>Sed id augue vitae urna euismod commodo aliquet a quam. Pellentesque arcu velit, cursus et malesuada ut, consequat et diam. Nullam erat sem, rhoncus id ullamcorper vitae, rhoncus et arcu. In ultricies ultricies nulla, ut rutrum nisi iaculis at. Donec eu magna a metus ornare faucibus. Fusce aliquet faucibus ultricies. Morbi semper, est id tincidunt gravida, sem arcu adipiscing lacus, ac bibendum nulla leo eu purus. Quisque nec diam sed risus consectetur a ccumsan quis quis nibh. Vestibulum id purus lorem.</p>
      <p>It is a long established fact that a reader will be distracted by the readable content of a page when looking at its layout. The point of using Lorem Ipsum is that it has a more-or-less normal distribution of letters, as opposed to using 'Content here, content here', making it look like readable English. Many desktop publishing packages</p>
    </div>
    <p class="closing">Sincerely,</p>
    <div class="signature" role="img" aria-label="Handwritten signature of Martin Hale"></div>

    <address class="letter-footer" style="font-style:normal">
      2140 Larkspur Avenue, Halden, Oregon 97410<br>
      P. 555-014-2287 &nbsp;E. m.hale@nordvanesystems.com W. www.nordvanesystems.com
    </address>
  </section>

  <section class="sheet envelope-back">
    <svg class="envelope-flap" viewBox="0 0 531 74" aria-hidden="true">
      <path d="M0 0 H531 L526 30 Q519 74 478 74 H53 Q12 74 5 30 Z" fill="var(--brand)"/>
    </svg>
    <div class="flap-content">
      <div class="flap-name">Nordvane Systems</div>
      <div class="flap-url">www.nordvanesystems.com</div>
    </div>
  </section>

  <section class="sheet envelope-front">
    <div class="brand-lockup">
      <div class="brand-dot"></div>
      <div class="brand-name"><span>Nordvane Systems</span><span class="legal">Private Limited</span></div>
    </div>
    <address class="return-address">2140 Larkspur Avenue<br>Halden, Oregon 97410</address>
    <div class="watermark"></div>
  </section>

</body>
</html>
```